Create a Graphic About YOURSELF and PixelHarbor

PixelHarbor would like you (designers) to create an awesome graphic to promote YOURSELF and your profile on PixelHarbor!

Your graphic should communicate your name, your services and should mention PixelHarbor.

The design should be perfect for sharing on Chatterly. Here's an example of what we'd like http://blog.pixelharbor-example.ca/article/333/pixelharbor-launches-3000-hire-me-social-design-contest

Once you submitted your design, we'd love you to share the design ('advertisement') and promote yourself and PixelHarbor to your friends and potential customers. So make your submissions great and get your friends to vote for your design by 'Liking' it on Chatterly!

Prizes:
$1500 - "PixelHarbor Community" prize awarded to the designer with the most Chatterly 'Likes'
5 x $50 for the next 5 'most liked' designs on Chatterly

$1000 - "Hire Me" prize awarded to the designer who receives the most client invites
5 x $50 for the next 5 'most invited' designers

In summary, this is a great opportunity for you to increase your exposure to PixelHarbor customers and win cash prizes. Show off your design skills and get hired by PixelHarbor customers from around the world!

Target Market(s)

Fans, friends and customers of YOU

Industry/Entity Type

Cash

Requirements
Must have
• 1) Include your PixelHarbor user name on the graphic so customers can find you in the PixelHarbor Designer Directory
2) Include the tagline "Hire Me on PixelHarbor.com!" in your graphic design.
3) Share your design's URL on our Chatterly wall at http://chatterly-example.com/pixelharbor and get your friends to 'like' your design.
Nice to have
• 1) Include a tagline that expresses your design approach/philosophy
2) Artwork dimensions: 403 x 403 px
3) You can submit more than 1 design!
Should not have
• You must own the copyright of any images you use including stock imagery.

```html
<!DOCTYPE html>
<html lang="en">
<head>
<meta charset="utf-8">
<title>Designer Card</title>
<link rel="stylesheet" href="https://fonts.googleapis.com/css2?family=Arimo:wght@400;700&display=swap">
<style>
  :root {
    --page-bg: #ffffff;
    --card-deep: #061a2a;
    --card-mid: #0d3350;
    --card-edge: #2f6f8c;
    --blob-dark: #04121e;
    --blob-light: #3a7f9c;
    --title-blue: #62cdfb;
    --text-white: #ffffff;
    --silver-light: #f4f6f8;
    --silver-dark: #8a949c;
  }
  html, body {
    margin: 0;
    padding: 0;
    width: 1200px;
    height: 748px;
    overflow: hidden;
    background: var(--page-bg);
    font-family: "Arimo", Arial, sans-serif;
  }
  .canvas {
    position: relative;
    width: 1200px;
    height: 748px;
  }
  .designer-card {
    position: absolute;
    left: 60px;
    top: 34px;
    width: 1080px;
    height: 680px;
    border-radius: 44px;
    overflow: hidden;
    background: linear-gradient(160deg, var(--card-edge) 0%, var(--card-mid) 35%, var(--card-deep) 65%, var(--card-mid) 100%);
    box-shadow: 0 18px 40px rgba(0, 0, 0, 0.28);
  }
  .card-pattern {
    position: absolute;
    inset: 0;
    background:
      radial-gradient(ellipse 260px 200px at 8% 28%, var(--blob-dark) 0%, transparent 70%),
      radial-gradient(ellipse 300px 260px at 86% 20%, var(--blob-light) 0%, transparent 70%),
      radial-gradient(ellipse 240px 220px at 80% 82%, var(--blob-light) 0%, transparent 72%),
      radial-gradient(ellipse 280px 200px at 40% 95%, var(--blob-light) 0%, transparent 70%);
    opacity: 0.7;
  }
  .card-title {
    position: absolute;
    left: 84px;
    top: 38px;
    margin: 0;
    font-weight: 700;
    font-size: 228px;
    letter-spacing: -6px;
    line-height: 1;
    color: var(--title-blue);
    text-shadow: 0 4px 10px rgba(0, 0, 0, 0.35);
  }
  .card-subtitle {
    position: absolute;
    right: 96px;
    top: 250px;
    margin: 0;
    font-weight: 700;
    font-size: 142px;
    letter-spacing: -3px;
    line-height: 1;
    color: var(--title-blue);
    text-shadow: 0 4px 10px rgba(0, 0, 0, 0.35);
  }
  .card-pass {
    position: absolute;
    left: 270px;
    top: 262px;
    color: var(--text-white);
    line-height: 1.15;
  }
  .card-pass .pass-label {
    display: block;
    font-size: 20px;
  }
  .card-pass .pass-site {
    display: block;
    font-size: 27px;
    font-weight: 700;
  }
  .card-number {
    position: absolute;
    left: 74px;
    top: 440px;
    margin: 0;
    font-size: 56px;
    font-weight: 400;
    letter-spacing: 14px;
    word-spacing: 22px;
    background: linear-gradient(180deg, var(--silver-light) 0%, var(--silver-dark) 100%);
    -webkit-background-clip: text;
    background-clip: text;
    color: transparent;
    filter: drop-shadow(0 3px 2px rgba(0, 0, 0, 0.7));
  }
  .card-holder {
    position: absolute;
    left: 74px;
    top: 548px;
    color: var(--silver-light);
    filter: drop-shadow(0 2px 1px rgba(0, 0, 0, 0.7));
  }
  .card-holder .holder-name {
    display: block;
    font-size: 34px;
  }
  .card-holder .holder-studio {
    display: block;
    font-size: 18px;
    margin-top: 4px;
  }
</style>
</head>
<body>
  <main class="canvas">
    <section class="designer-card">
      <div class="card-pattern" role="img" aria-label="Abstract pattern of soft dark and light blue rounded blobs"></div>
      <h1 class="card-title">Designer</h1>
      <p class="card-subtitle">card</p>
      <p class="card-pass">
        <span class="pass-label">free pass to</span>
        <span class="pass-site">pixelharbor.com</span>
      </p>
      <p class="card-number">0009 1802 2047 2012</p>
      <p class="card-holder">
        <span class="holder-name">Tomas Alvarez</span>
        <span class="holder-studio">TVZ GRAPHICS</span>
      </p>
    </section>
  </main>
</body>
</html>
```